Magazine Advertisement Needed for Construction Finance Company

We need two separate full page magazine ads created for our company, LoanHarbor. The ad will be featured in Steelframe Builder magazine. The audience is made up of commercial construction professionals. We want the ad to feel uplifting and empowering, as well as provide a general overview of our business along with a testimonial.
Key points for page 1:
header: Building Better Businesses, Communities, and Lives.
testimonial: "With the help of LoanHarbor, we were able to compete, and ultimately win our bid. With such limited funding options out there for us construction guys, it was a breath of fresh air when we discovered what they're doing at LoanHarbor." - Lorenzo Bassanelli, Owner and President, T.R.O.N. Precast
pitch: Discover what we're doing at LoanHarbor
www.loanharbor.example/sbmag
+1 (866) 555-0147
Key points for page 2:
header: Funding the Construction Industry
bullets:
- Revolving Credit Lines from $15K to $5MM
- Net 10 Discounts with Suppliers of Your Choice
- 150 Day Terms
- No ScoreTrak Needed, No Hidden Fees
body: Whether you are looking to free up your existing capital to make room for growth, or need to extend the period of time between paying for supplies and receiving your draws - LoanHarbor gives you the freedom to succeed.
Take your business to the next level today!
+1 (866) 555-0147
Here are links to our website and the magazine for references:
Our site: http://loanharbor.example/
Magazine: http://www.steelframebuilder.example/magazine/
Feel free to checkout our social networks for some additional information/inspiration.
Specs:
Full Page Ad With Bleed
Live Area: 7.5" x 10"
Bleed Size: 8.25" x 10.75"
Safety: .25" from trim on all sides
Bleed: add .125" to all four sides
PDF/X-1a 2001 files required. Set up files for 4/C process printing with all fonts and images embedded. All images must be high resolution (300 dpi for CMYK and grayscale images and 600 DPI for line art). Place images at 100% to ensure better reproduction. Offset crop and trim marks by 1/8" so that they do not extend into bleed or live area. Line screen: 133. Please follow SWOP standards.

```html
<!DOCTYPE html>
<html lang="en">
<head>
<meta charset="utf-8">
<title>LoanHarbor — Funding the Construction Industry</title>
<link rel="stylesheet" href="https://fonts.googleapis.com/css2?family=Jost:wght@700&family=Questrial&family=Open+Sans:wght@700&display=swap">
<style>
  :root {
    --backdrop: #e6e8ea;
    --page: #ffffff;
    --ink: #111111;
    --ink-soft: #2a2a2a;
    --accent-blue: #4a8fe0;
    --brand-dark: #161616;
    --money-green: #8fae86;
    --money-deep: #4f7a4c;
    --sand: #b49a80;
  }
  * { box-sizing: border-box; margin: 0; padding: 0; }
  html, body {
    width: 1200px; height: 1200px; overflow: hidden;
    background: var(--backdrop);
  }
  .ad-page {
    position: absolute; left: 166px; top: 22px;
    width: 868px; height: 1156px;
    background: var(--page);
    box-shadow: 0 0 0 1px rgba(0,0,0,0.12);
    overflow: hidden;
  }
  .headline {
    position: absolute; top: 92px; left: 0; width: 100%;
    text-align: center;
    font-family: "Jost", sans-serif; font-weight: 700;
    font-size: 33px; color: var(--ink); letter-spacing: 0.2px;
  }
  .hero-art {
    position: absolute; left: 102px; top: 202px; width: 688px; height: 322px;
    border-radius: 40px;
    background:
      radial-gradient(ellipse 18% 30% at 86% 45%, var(--sand) 0%, rgba(180,154,128,0.6) 60%, rgba(255,255,255,0) 100%),
      radial-gradient(ellipse 45% 45% at 32% 48%, var(--money-deep) 0%, var(--money-green) 55%, rgba(255,255,255,0) 100%),
      var(--page);
  }
  .feature-list {
    position: absolute; left: 204px; top: 560px;
    list-style: none;
    font-family: "Questrial", sans-serif; font-size: 19.5px; color: var(--ink-soft);
    white-space: nowrap;
  }
  .feature-list li { line-height: 29px; }
  .feature-list li:last-child { margin-top: 5px; }
  .pitch {
    position: absolute; left: 204px; top: 717px;
    font-family: "Questrial", sans-serif; font-size: 18.5px; line-height: 33.6px;
    color: var(--ink-soft); white-space: nowrap;
  }
  .call-to-action {
    position: absolute; top: 893px; left: 0; width: 100%;
    text-align: center;
    font-family: "Questrial", sans-serif; font-size: 23.5px; color: var(--ink);
  }
  .contact {
    position: absolute; left: 234px; width: 400px; top: 1088px;
    text-align: center;
    font-family: "Open Sans", sans-serif; font-weight: 700;
    font-size: 17px; line-height: 23px; color: var(--accent-blue);
  }
  .brand {
    position: absolute; left: 600px; top: 958px; width: 252px;
    text-align: center;
  }
  .brand-dot { display: block; margin: 0 auto 22px; }
  .brand-name {
    font-family: "Questrial", sans-serif; font-size: 31px; color: var(--brand-dark);
  }
</style>
</head>
<body>
  <main class="ad-page">
    <h1 class="headline">Funding the Construction Industry</h1>

    <div class="hero-art" role="img" aria-label="Photo of an excavator folded from dollar bills digging toward a small pile of sand"></div>

    <ul class="feature-list">
      <li>-Revolving Credit Lines from $15K to $5MM</li>
      <li>- Net 10 Discounts with Suppliers of Your Choice</li>
      <li>- 150 Day Terms</li>
      <li>- No ScoreTrak Needed, No Hidden Fees</li>
    </ul>

    <p class="pitch">Whether you are looking to free up your existing capital<br>to make room for growth, or need to extend the period<br>of time between paying for supplies and receiving your<br>draws -LoanHarbor gives you the freedom to succeed.</p>

    <p class="call-to-action">Take your business to the next level today!</p>

    <div class="contact">
      <div>loanharbor.example/sbmag</div>
      <div>+1 (866) 555-0147</div>
    </div>

    <div class="brand">
      <svg class="brand-dot" width="114" height="114" viewBox="0 0 114 114" aria-hidden="true">
        <circle cx="57" cy="57" r="55" fill="var(--accent-blue)"/>
      </svg>
      <div class="brand-name">LoanHarbor</div>
    </div>
  </main>
</body>
</html>
```